Business card for Mortgage broker business

I have already had the logo designed and am needing a great looking business card. My business focus is on servicing clients who may not be able to obtain finance through traditional lenders due to bad credit, short term employment or they just don't fit the banks profile. It needs to be professional, trust worthy but also have a caring fell about it.
I have provided files showing the green and black logo, the white logo(on white background so the file looks blank) and also a file with the white logo with a background of leaves that was made up which will probably be used for a website header.

Industry/Entity Type

Finance

Contact Information for Business Card

Marcus Dalby
Managing Director, Accredited Finance Broker(AFB)
Po Box 817, Pakenham VIC 3810
marcus@kestrelfunding.com.au
www.kestrelfunding.com.au
0438 216 507

Requirements
Nice to have
• I have added a picture of myself as I would like to see some designs with the pic in it, but I'm not sure if I want it on there with the logo's or just the logo's

```html
<!DOCTYPE html>
<html lang="en">
<head>
<meta charset="utf-8">
<title>Kestrel Funding — Business Card</title>
<link rel="stylesheet" href="https://fonts.googleapis.com/css2?family=Montserrat:wght@400;500;700&display=swap">
<style>
  :root {
    --page-bg: #e9ebea;
    --brand-green: #075f33;
    --ink-dark: #13201c;
    --paper: #ffffff;
    --ring-grey: #3a3f3d;
    --text-light: #ffffff;
  }
  * { margin: 0; padding: 0; box-sizing: border-box; }
  html, body {
    width: 1200px;
    height: 900px;
    overflow: hidden;
    background: var(--page-bg);
    font-family: "Montserrat", Arial, sans-serif;
  }
  .canvas {
    width: 1200px;
    height: 900px;
    display: flex;
    flex-direction: column;
    align-items: center;
    justify-content: center;
    gap: 60px;
  }
  .card {
    width: 630px;
    height: 360px;
    position: relative;
    overflow: hidden;
    box-shadow: 0 8px 22px rgba(0, 0, 0, 0.14);
  }
  .card-front {
    background: var(--brand-green);
    display: flex;
    align-items: center;
    justify-content: center;
  }
  .brand-name {
    font-family: "Montserrat", Arial, sans-serif;
    font-weight: 700;
    letter-spacing: 0.02em;
    white-space: nowrap;
  }
  .card-front .brand-name {
    color: var(--text-light);
    font-size: 46px;
  }
  .card-back { background: var(--paper); }
  .card-back svg.back-art {
    position: absolute;
    inset: 0;
  }
  .contact-name {
    position: absolute;
    left: 290px;
    top: 112px;
    color: var(--text-light);
    font-weight: 700;
    font-size: 30px;
  }
  .contact-line {
    position: absolute;
    left: 240px;
    color: var(--text-light);
    font-weight: 400;
    font-size: 15px;
    white-space: nowrap;
  }
  .line-phone { top: 178px; }
  .line-email { top: 208px; left: 285px; }
  .line-web { top: 238px; left: 330px; }
  .card-back .brand-name {
    position: absolute;
    left: 50px;
    top: 282px;
    color: var(--brand-green);
    font-size: 32px;
  }
</style>
</head>
<body>
<main class="canvas">
  <section class="card card-front" aria-label="Card front">
    <span class="brand-name">Kestrel Funding</span>
  </section>

  <section class="card card-back" aria-label="Card back">
    <svg class="back-art" width="630" height="360" viewBox="0 0 630 360" aria-hidden="true">
      <polygon points="0,0 630,0 630,360 470,360 0,50" fill="var(--ink-dark)"/>
      <line x1="0" y1="64" x2="450" y2="362" stroke="var(--ink-dark)" stroke-width="4"/>

      <g class="icon icon-phone" transform="translate(190,186)">
        <circle r="16" fill="var(--paper)" stroke="var(--ring-grey)" stroke-width="5"/>
        <path d="M-7,-3 Q0,-9 7,-3 L5,0 L2,-2 L-2,-2 L-5,0 Z M-6,2 H6 V6 H-6 Z" fill="var(--brand-green)"/>
      </g>
      <g class="icon icon-mail" transform="translate(235,216)">
        <circle r="16" fill="var(--paper)" stroke="var(--ring-grey)" stroke-width="5"/>
        <rect x="-7" y="-5" width="14" height="10" fill="var(--brand-green)"/>
        <path d="M-7,-5 L0,1 L7,-5" fill="none" stroke="var(--paper)" stroke-width="1.2"/>
      </g>
      <g class="icon icon-link" transform="translate(280,246)">
        <circle r="16" fill="var(--paper)" stroke="var(--ring-grey)" stroke-width="5"/>
        <g fill="none" stroke="var(--brand-green)" stroke-width="2.4" transform="rotate(-45)">
          <rect x="-8" y="-3.5" width="9" height="7" rx="3.5"/>
          <rect x="-1" y="-3.5" width="9" height="7" rx="3.5"/>
        </g>
      </g>
    </svg>

    <h1 class="contact-name">Marcus Dalby</h1>
    <p class="contact-line line-phone">0438 216 507</p>
    <p class="contact-line line-email">marcus@kestrelfunding.com.au</p>
    <p class="contact-line line-web">www.kestrelfunding.com.au</p>

    <span class="brand-name">Kestrel Funding</span>
  </section>
</main>
</body>
</html>
```